needs to stand out, but be very clean
Project: Logo for auto broker stationary,
Logo for auto broker stationary,  - Automotive
Logo for auto broker stationary,
Professional
Harbor Motorworks USA
Los Angeles based, Global shipping
Dorian@harbormotorworks-example.com
www.harbormotorworks-example.com
I would like to have at least one file in vector eps, logo and cards. I would like 4 or 6 automotive logos in the corners (4) velorian, Kastra, Tenko, Ardello or (6) Velorian, Kastra, Ardello, Tenko, Ardello, Quellano the other two in the middle of top and bottom. If you like the initials HMU you can use them. working on getting 800 number now, please just put in 555-014-2731 and we can change it later. I was thinking black background for card with white or silver writing and maybe some kind of splash of red.
Pick a font or style you like saying: You don't go to court without an attorney. Why would you buy a car without your Broker?
DorianPlume DorianPlume
I'm surprised that only one person actually read what I wrote and showed me one business card with car logos (kastra, velorian etc. ) on it. I think I like the logo centered.

```html
<!DOCTYPE html>
<html lang="en">
<head>
<meta charset="utf-8">
<title>Harbor Motorworks USA – Business Cards</title>
<link rel="stylesheet" href="https://fonts.googleapis.com/css2?family=Cinzel:wght@400;600&family=Arimo:wght@400&display=swap">
<style>
  :root {
    --backdrop: #ece4d6;
    --card-red: #e8222b;
    --card-black: #0b0b0b;
    --ink-white: #ffffff;
    --divider: #5a5a5a;
  }
  * { box-sizing: border-box; margin: 0; padding: 0; }
  html, body { width: 1200px; height: 852px; overflow: hidden; }
  body { background: var(--backdrop); position: relative; font-family: "Arimo", Arial, sans-serif; }

  .business-card {
    position: absolute;
    width: 540px;
    height: 300px;
    border-radius: 18px;
    overflow: hidden;
    display: flex;
    box-shadow: 0 6px 16px rgba(0,0,0,0.22);
  }
  .card-front { left: 110px; top: 110px; }
  .card-back  { left: 550px; top: 442px; }

  .info-panel {
    width: 47%;
    background: var(--card-red);
    color: var(--ink-white);
    padding: 52px 26px 0 26px;
  }
  .brand-panel {
    width: 53%;
    background: var(--card-black);
    display: flex;
    align-items: center;
    justify-content: center;
  }
  .card-front .brand-panel { border-left: 2px solid var(--divider); }
  .card-back .brand-panel { border-right: 2px solid var(--divider); }
  .card-back .info-panel { text-align: right; }

  .person-name {
    font-family: "Cinzel", Georgia, serif;
    font-weight: 600;
    font-size: 17px;
    letter-spacing: 0.5px;
  }
  .person-title {
    font-family: "Cinzel", Georgia, serif;
    font-size: 13px;
    margin-top: 3px;
  }
  .tagline {
    font-size: 10.5px;
    line-height: 1.45;
    margin-top: 16px;
  }
  .contact-list { list-style: none; margin-top: 18px; }
  .contact-list li {
    display: flex;
    align-items: center;
    gap: 7px;
    font-size: 9.5px;
    line-height: 1.2;
    margin-bottom: 5px;
    white-space: nowrap;
  }
  .card-back .contact-list li { flex-direction: row-reverse; }
  .contact-icon { width: 11px; height: 11px; flex: none; }

  .brand-name {
    font-family: "Cinzel", Georgia, serif;
    font-weight: 600;
    color: var(--ink-white);
    font-size: 21px;
    letter-spacing: 1px;
    text-align: center;
    line-height: 1.25;
  }
</style>
</head>
<body>

<svg width="0" height="0" style="position:absolute" aria-hidden="true">
  <defs>
    <symbol id="icon-phone" viewBox="0 0 24 24"><path fill="#fff" d="M6.6 10.8a15 15 0 0 0 6.6 6.6l2.2-2.2a1 1 0 0 1 1-.25 11.4 11.4 0 0 0 3.6.57 1 1 0 0 1 1 1V20a1 1 0 0 1-1 1A17 17 0 0 1 3 4a1 1 0 0 1 1-1h3.5a1 1 0 0 1 1 1c0 1.25.2 2.45.57 3.57a1 1 0 0 1-.25 1z"/></symbol>
    <symbol id="icon-mobile" viewBox="0 0 24 24"><rect x="6" y="2" width="12" height="20" rx="2" fill="none" stroke="#fff" stroke-width="2.2"/><circle cx="12" cy="18" r="1.3" fill="#fff"/></symbol>
    <symbol id="icon-mail" viewBox="0 0 24 24"><rect x="2" y="5" width="20" height="14" rx="1.5" fill="#fff"/><path d="M3 6l9 7 9-7" fill="none" stroke="#e8222b" stroke-width="1.8"/></symbol>
    <symbol id="icon-globe" viewBox="0 0 24 24"><circle cx="12" cy="12" r="9.5" fill="none" stroke="#fff" stroke-width="2"/><path d="M2.5 12h19M12 2.5c3 3 3 16 0 19M12 2.5c-3 3-3 16 0 19" fill="none" stroke="#fff" stroke-width="1.6"/></symbol>
  </defs>
</svg>

<article class="business-card card-front">
  <section class="info-panel">
    <h1 class="person-name">Dorian Plume</h1>
    <p class="person-title">Managing Director</p>
    <p class="tagline">Los Angeles based<br>Global shipping</p>
    <ul class="contact-list">
      <li><svg class="contact-icon"><use href="#icon-phone"/></svg>1 555 014 2731(T)</li>
      <li><svg class="contact-icon"><use href="#icon-mobile"/></svg>555-014-2298</li>
      <li><svg class="contact-icon"><use href="#icon-mail"/></svg>Dorian@harbormotorworks-example.com</li>
      <li><svg class="contact-icon"><use href="#icon-globe"/></svg>www.harbormotorworks-example.com</li>
    </ul>
  </section>
  <section class="brand-panel">
    <p class="brand-name">Harbor Motorworks<br>USA</p>
  </section>
</article>

<article class="business-card card-back">
  <section class="brand-panel">
    <p class="brand-name">Harbor Motorworks<br>USA</p>
  </section>
  <section class="info-panel">
    <h2 class="person-name">Dorian Plume</h2>
    <p class="person-title">Managing Director</p>
    <p class="tagline">Los Angeles based<br>Global shipping</p>
    <ul class="contact-list">
      <li><svg class="contact-icon"><use href="#icon-phone"/></svg>1 555 014 2731(T)</li>
      <li><svg class="contact-icon"><use href="#icon-mobile"/></svg>555-014-2298</li>
      <li><svg class="contact-icon"><use href="#icon-mail"/></svg>Dorian@harbormotorworks-example.com</li>
      <li><svg class="contact-icon"><use href="#icon-globe"/></svg>www.harbormotorworks-example.com</li>
    </ul>
  </section>
</article>

</body>
</html>
```